Harrowgate Supply Group Business Card Design

The Business Card will be one side only with Harrowgate Supplies Group Logo
Card should have:
Name
Title
Office phone Number
Cell Number
email address
Website
Street Address
Our Slogan is Sturdy and Steadfast
Looking for something that stands out from other business cards

Target Market(s)

Heavy equipment Lease Company

```html
<!DOCTYPE html>
<html lang="en">
<head>
<meta charset="utf-8">
<title>Harrowgate Supplies Group – Business Card</title>
<link rel="stylesheet" href="https://fonts.googleapis.com/css2?family=Work+Sans:wght@400;500;700&display=swap">
<style>
  :root {
    --stage: #3b3b3d;
    --red: #d0142a;
    --red-deep: #b80f22;
    --navy: #2b2d7c;
    --white: #ffffff;
  }
  * { box-sizing: border-box; margin: 0; padding: 0; }
  html, body { width: 1200px; height: 900px; overflow: hidden; }
  body {
    background: var(--stage);
    font-family: "Work Sans", Arial, sans-serif;
    position: relative;
  }
  .card {
    position: absolute;
    overflow: hidden;
    box-shadow: 0 14px 30px rgba(0,0,0,.45);
  }

  /* Front: portrait contact card */
  .card-front {
    left: 130px; top: 180px;
    width: 310px; height: 540px;
    background: var(--red);
  }
  .card-front .backdrop { position: absolute; inset: 0; }
  .front-content { position: relative; padding: 34px 30px; color: var(--white); }
  .brand { display: flex; align-items: flex-start; gap: 10px; }
  .brand-mark { width: 22px; height: 22px; background: var(--navy); flex: none; margin-top: 2px; }
  .brand-name {
    font-weight: 700; font-size: 19px; line-height: 1.15;
    text-transform: uppercase; color: var(--white);
  }
  .brand-sub {
    display: block; margin-top: 4px;
    font-size: 11px; letter-spacing: .55em; color: var(--navy);
    border-top: 1.5px solid var(--navy); padding-top: 3px; width: 190px;
  }
  .person { margin-top: 30px; }
  .person-name {
    font-size: 17px; font-weight: 500; color: var(--navy);
    text-transform: uppercase; letter-spacing: .04em;
  }
  .person-title { font-size: 12px; margin-top: 2px; }
  .address { font-size: 12px; line-height: 1.45; margin-top: 14px; }
  .contact-list { list-style: none; margin-top: 12px; font-size: 12px; line-height: 1.6; }
  .contact-list li { display: flex; align-items: center; gap: 7px; }
  .contact-list svg { width: 10px; height: 10px; fill: var(--white); flex: none; }

  /* Back: landscape brand card */
  .card-back {
    left: 500px; top: 230px;
    width: 560px; height: 320px;
    background: linear-gradient(135deg, var(--red) 0%, var(--red-deep) 100%);
    color: var(--white);
    display: flex; flex-direction: column; justify-content: center; align-items: center;
  }
  .back-brand { display: flex; align-items: center; gap: 14px; }
  .back-brand .brand-mark { width: 30px; height: 30px; background: var(--white); margin: 0; }
  .back-brand .brand-name { font-size: 32px; letter-spacing: .02em; }
  .slogan {
    margin-top: 22px;
    font-size: 15px; letter-spacing: .22em; text-transform: uppercase; font-weight: 400;
  }
</style>
</head>
<body>

<section class="card card-front" aria-label="Business card front">
  <svg class="backdrop" viewBox="0 0 310 540" preserveAspectRatio="none" aria-hidden="true">
    <polygon points="310,270 310,540 130,540 210,330" fill="var(--white)"/>
    <polygon points="0,420 150,400 130,540 0,540" fill="var(--red-deep)" opacity=".35"/>
  </svg>
  <div class="front-content">
    <div class="brand">
      <span class="brand-mark"></span>
      <p class="brand-name">Harrowgate Supplies<span class="brand-sub">GROUP</span></p>
    </div>
    <div class="person">
      <p class="person-name">Daniel Hart</p>
      <p class="person-title">Director</p>
    </div>
    <p class="address">412b Kestrel Road,<br>Ashby, NZ, 8024</p>
    <ul class="contact-list">
      <li><svg viewBox="0 0 10 10"><path d="M2 0h2l1 3-1.5 1a6 6 0 0 0 2.5 2.5L7 5l3 1v2c0 1-1 2-2 2A8 8 0 0 1 0 2c0-1 1-2 2-2z"/></svg>(555) 210-4471</li>
      <li><svg viewBox="0 0 10 10"><rect x="2.5" y="0" width="5" height="10" rx="1"/></svg>(555) 318-2096</li>
      <li><svg viewBox="0 0 10 10"><path d="M0 2h10v6H0zM0 2l5 3.5L10 2" stroke="var(--red)" stroke-width=".8"/></svg>hello@harrowgategroup.com</li>
      <li><svg viewBox="0 0 10 10"><circle cx="5" cy="5" r="5"/></svg>www.harrowgategroup.com</li>
    </ul>
  </div>
</section>

<section class="card card-back" aria-label="Business card back">
  <div class="back-brand">
    <span class="brand-mark"></span>
    <p class="brand-name">Harrowgate Pumps</p>
  </div>
  <p class="slogan">Sturdy and Steadfast</p>
</section>

</body>
</html>
```